emerald card

Belvardi/Gems
Est.1972
We are a direct Importer of Colombian Emeralds, with gem lab certificates KSR,PMB 1.0ct. and over.Gem ID and Country of origin
Hal Belvardi belvo@postwing.example
469 555 0176 www. belvardiline.example
The current web page is being redesigned,please ,Belvardi/Gems is a new company. We specialize in Colombian Emeralds.
Some of the designers used the existing web page and companies and created business cards for the wrong companies.
The blue back ground deign from Sri Lanka is the only card design that has all the correct information.

Target Market(s)

Fine Jewelry

Industry/Entity Type

Business

Contact Information for Business Card

Belvardi/Gems

Font styles to use
Other font styles liked:
• Roman

Requirements
Must have
• Belvardi/Gems Hal Belvardi
P.O.Box 318270 Dallas,Tx.75908 Ph. 469 555 0176 E-Mail:belvo@postwing.example
www.belvardiline.example, Emeralds over 1.0ct. are certified for Country of origin and Gem ID-KSR or PMB cerificates.

We are importers of Colombian Emeralds all Emeralds over 1.0ct.
Dallas,Tx. 75908
KSR,PMB
Nice to have
• Picture of Emerald
Should not have
• No other company names
We are changing information on our web site.do not use the web page for design.

```html
<!DOCTYPE html>
<html lang="en">
<head>
<meta charset="utf-8">
<title>Belvardi/Gems – Business Card</title>
<link href="https://fonts.googleapis.com/css2?family=Cinzel:wght@400;500&display=swap" rel="stylesheet">
<style>
  :root {
    --backdrop: #e6e6e6;
    --card: #ffffff;
    --green-bright: #1c9a57;
    --green-deep: #136b40;
    --gem-light: #2fae6a;
    --gem-mid: #167a45;
    --gem-dark: #0a3d22;
  }
  * { margin: 0; padding: 0; box-sizing: border-box; }
  html, body {
    width: 992px; height: 1200px; overflow: hidden;
    background: var(--backdrop);
    font-family: "Cinzel", "Times New Roman", serif;
    font-weight: 400;
  }
  .canvas { position: relative; width: 992px; height: 1200px; }
  .card {
    position: absolute; left: 75px; width: 870px; height: 495px;
    background: var(--card); border-radius: 24px;
  }
  .card--front { top: 68px; }
  .card--back { top: 627px; }

  .person-name {
    position: absolute; left: 0; width: 100%;
    text-align: center; color: var(--green-bright);
    font-size: 46px; letter-spacing: 1px; line-height: 1; font-weight: 400;
  }
  .card--front .person-name { top: 22px; padding-left: 60px; }
  .established {
    position: absolute; top: 82px; left: 0; width: 100%; padding-left: 60px;
    text-align: center; color: var(--green-deep); font-size: 27px; line-height: 1;
  }

  .contact-list { position: absolute; left: 60px; top: 148px; list-style: none; }
  .contact-item {
    display: flex; align-items: center; height: 48px;
    color: var(--green-deep); font-size: 24px; letter-spacing: 0.5px;
    text-transform: uppercase; white-space: nowrap;
  }
  .contact-item--small { font-size: 20px; }
  .contact-item svg { width: 22px; height: 22px; margin-right: 40px; fill: var(--green-deep); flex: none; }

  .gem-field {
    position: absolute; left: 64px; color: var(--green-bright);
    font-size: 26px; white-space: nowrap; line-height: 1;
  }
  .gem-field--id { top: 378px; }
  .gem-field--origin { top: 438px; }
  .gem-field .fill-line {
    display: inline-block; height: 18px; vertical-align: baseline;
    border-bottom: 2px dotted var(--green-deep);
  }
  .gem-field--id .fill-line { width: 336px; }
  .gem-field--origin .fill-line { width: 168px; }

  .gem-photo {
    position: absolute;
    background: radial-gradient(circle at 50% 50%, var(--gem-light) 0%, var(--gem-mid) 45%, var(--gem-dark) 100%);
    clip-path: polygon(12% 0, 88% 0, 100% 12%, 100% 88%, 88% 100%, 12% 100%, 0 88%, 0 12%);
  }
  .card--front .gem-photo { left: 610px; top: 242px; width: 204px; height: 200px; }
  .card--back .gem-photo { left: 337px; top: 48px; width: 194px; height: 192px; }

  .card--back .person-name { top: 290px; font-size: 48px; }
  .company-name {
    position: absolute; top: 360px; left: 0; width: 100%;
    text-align: center; color: var(--green-deep); font-size: 24px; letter-spacing: 1px;
  }
  .certification {
    position: absolute; top: 404px; left: 60px; right: 60px;
    text-align: center; color: var(--green-deep); font-size: 15px; line-height: 1.6;
  }
</style>
</head>
<body>
<main class="canvas">

  <section class="card card--front">
    <h1 class="person-name">Hal Belvardi</h1>
    <p class="established">Est.1972</p>

    <ul class="contact-list">
      <li class="contact-item contact-item--small">
        <svg viewBox="0 0 24 24" aria-hidden="true"><path d="M12 2a7 7 0 0 0-7 7c0 5.2 7 13 7 13s7-7.8 7-13a7 7 0 0 0-7-7zm0 9.5A2.5 2.5 0 1 1 12 6.5a2.5 2.5 0 0 1 0 5z"/></svg>
        P.O.Box 318270 Dallas, Tx. 75908
      </li>
      <li class="contact-item">
        <svg viewBox="0 0 24 24" aria-hidden="true"><path d="M12 2a10 10 0 1 0 0 20 10 10 0 0 0 0-20zm0 1.8c1.2 1.3 2.1 3.3 2.4 5.2H9.6c.3-1.9 1.2-3.9 2.4-5.2zM9.4 4.3C8.6 5.7 8 7.3 7.8 9H4.4a8.2 8.2 0 0 1 5-4.7zm5.2 0a8.2 8.2 0 0 1 5 4.7h-3.4c-.2-1.7-.8-3.3-1.6-4.7zM4 10.8h3.7v2.4H4v-2.4zm5.5 0h5v2.4h-5v-2.4zm6.8 0H20v2.4h-3.7v-2.4zM4.4 15h3.4c.2 1.7.8 3.3 1.6 4.7a8.2 8.2 0 0 1-5-4.7zm5.2 0h4.8c-.3 1.9-1.2 3.9-2.4 5.2-1.2-1.3-2.1-3.3-2.4-5.2zm6.6 0h3.4a8.2 8.2 0 0 1-5 4.7c.8-1.4 1.4-3 1.6-4.7z"/></svg>
        belvo@postwing.example
      </li>
      <li class="contact-item">
        <svg viewBox="0 0 24 24" aria-hidden="true"><path d="M6.6 2.5l2.6 3.9-1.7 2c1 2.6 3.5 5.2 6.1 6.3l2-1.7 3.9 2.6-1.6 3.4c-6.8.2-14.2-7.5-13.9-14.3z"/></svg>
        469 555 0176
      </li>
      <li class="contact-item">
        <svg viewBox="0 0 24 24" aria-hidden="true"><path d="M12 2l5 5-3 3-2-2 3-1-3-3-5 5 3 3-2 2-5-5zm0 20l-5-5 3-3 2 2-3 1 3 3 5-5-3-3 2-2 5 5z"/></svg>
        www.belvardiline.example
      </li>
    </ul>

    <p class="gem-field gem-field--id">Gem ID : <span class="fill-line"></span></p>
    <p class="gem-field gem-field--origin">Country of origin : <span class="fill-line"></span></p>

    <div class="gem-photo" role="img" aria-label="Photo of an emerald-cut green emerald"></div>
  </section>

  <section class="card card--back">
    <div class="gem-photo" role="img" aria-label="Photo of an emerald-cut green emerald"></div>
    <h2 class="person-name">Hal Belvardi</h2>
    <p class="company-name">Belvardi/Gems</p>
    <p class="certification">Importers of Colombian Emeralds · Emeralds over 1.0ct. are certified<br>for Country of origin and Gem ID – KSR or PMB certificates</p>
  </section>

</main>
</body>
</html>
```